Copper Lantern Consulting Wordpress Website Design

I am looking for a wordpress website design for a consulting company called Copper Lantern Consulting. Services include SEO, social media campaign, PPC, and other online services. I want a media savvy looking website that is very easy to navigate but still looks professional. I'm essentially looking to have the clients say "wow" when they see the website but still can get an idea of the services they offer as a company. colour scheme should be blue and white primarily as the logo will be blue and white (in the midst of getting it finalized).

Target Market(s)

B2B, business owners and decision makers for SEO, PPC, Social Media, Etc.

Industry/Entity Type

Business Consultant

Colors
0293ce
33a6d7
0255a3
3276b5
85acd3
ffffff

Requirements
Must have
• Must look sleek and "techy" but at the same time look stylish and media savvy.
Nice to have
• blue and white as the colour scheme to a degree. Just an idea considering the logo will be blue and white. Perhaps some nice high resolution photos, some sliders
• also looking for potentially having large icons that represent some of the services we provide so its easy for clients to know what we offer.
Should not have
• bubbly and fun. This is more of a professional website.

```html
<!DOCTYPE html>
<html lang="en">
<head>
<meta charset="utf-8">
<title>Copper Lantern Consulting</title>
<link rel="stylesheet" href="https://fonts.googleapis.com/css2?family=Ubuntu:wght@400;500;700&family=Open+Sans:wght@400;600;700&display=swap">
<style>
:root{
  --blue:#0293ce;
  --blue-light:#33a6d7;
  --blue-deep:#0255a3;
  --blue-mid:#3276b5;
  --blue-soft:#85acd3;
  --white:#ffffff;
  --ink:#2b2f33;
  --text:#6b7177;
  --line:#e3e6e9;
  --pale:#f4f6f8;
  --dark:#1e2730;
}
*{box-sizing:border-box;margin:0;padding:0}
html,body{width:1200px;height:2692px;overflow:hidden}
body{font-family:"Open Sans",Arial,sans-serif;color:var(--text);background:var(--white);font-size:13px;line-height:1.6}
h1,h2,h3,h4{font-family:"Ubuntu",Arial,sans-serif;font-weight:500;color:var(--ink)}
.wrap{width:960px;margin:0 auto;position:relative}

/* header */
.site-header{height:110px;background:var(--white);border-bottom:1px solid var(--line)}
.site-header .wrap{display:flex;align-items:center;justify-content:space-between;height:110px}
.brand{display:flex;align-items:center;gap:10px;font-family:"Ubuntu",sans-serif;font-weight:500;font-size:19px;color:var(--blue-deep)}
.brand-square{width:34px;height:34px;background:var(--blue-deep)}
.main-nav{display:flex}
.main-nav a{font-size:11px;font-weight:600;color:#555;text-decoration:none;letter-spacing:.5px;padding:0 18px;border-left:1px solid var(--line)}
.main-nav a:first-child{border-left:0}

/* hero */
.hero{height:550px;position:relative;overflow:hidden}
.hero-photo{position:absolute;inset:0;background:linear-gradient(100deg,#c9d3dc 0%,#dfe5ea 35%,#9aa9b8 62%,#5d6d7e 100%)}
.hero-copy{position:absolute;left:120px;top:150px;width:340px}
.hero-copy h1{color:var(--white);font-weight:700;font-size:30px;line-height:1.1;letter-spacing:.5px}
.hero-copy h1 span{display:block;font-size:54px;color:var(--blue)}
.hero-copy p{color:var(--white);font-size:12px;margin-top:14px;line-height:1.5}
.slide-arrow{position:absolute;top:255px;width:30px;height:40px;background:rgba(0,0,0,.45);display:flex;align-items:center;justify-content:center}
.slide-arrow.prev{left:0}.slide-arrow.next{right:0}

/* welcome */
.welcome{height:160px;padding-top:36px;border-bottom:8px solid var(--pale)}
.welcome h2{font-size:32px}
.welcome h2 span{color:var(--blue)}
.welcome p{font-size:12px;margin-top:10px;width:960px}
.btn{display:inline-block;background:var(--blue);color:var(--white);font-size:11px;font-weight:600;padding:9px 26px;text-decoration:none;letter-spacing:.5px}
.welcome .btn{position:absolute;right:0;top:4px}

/* services */
.services{height:490px;padding-top:48px;text-align:center}
.services h2{font-size:36px;font-weight:400}
.services .intro{width:720px;margin:12px auto 0;font-size:12px}
.service-grid{display:flex;justify-content:space-between;margin-top:44px}
.service{width:210px}
.service-icon{width:104px;height:104px;border-radius:50%;background:var(--blue);margin:0 auto;display:flex;align-items:center;justify-content:center}
.service h3{font-family:"Open Sans",sans-serif;font-size:13px;font-weight:600;margin-top:22px;color:#444}
.service p{font-size:11.5px;margin-top:8px}

/* testimonial */
.testimonial{height:290px;position:relative;margin-top:20px;text-align:center;color:var(--white)}
.testimonial-photo{position:absolute;inset:0;background:linear-gradient(180deg,#26313b 0%,#3a4652 55%,#1c252d 100%)}
.testimonial .wrap{padding-top:42px}
.quote-mark{font-family:"Ubuntu",sans-serif;font-size:64px;line-height:1;font-weight:700}
.testimonial p{width:820px;margin:14px auto 0;font-size:12.5px;color:#e6ebef}
.dots{display:flex;gap:8px;justify-content:center;margin-top:22px}
.dots i{width:10px;height:10px;border-radius:50%;background:#8a949c}
.dots i.on{background:var(--blue)}
.t-arrow{position:absolute;top:140px;font-size:28px;color:#cfd6dc}
.t-arrow.prev{left:-10px}.t-arrow.next{right:-10px}

/* team */
.team{height:320px;padding-top:40px}
.team-grid{display:flex;justify-content:space-between}
.member{width:228px;border:1px solid var(--line);padding:8px;text-align:center;background:var(--white)}
.member-photo{height:180px;background:linear-gradient(180deg,#dfe4e8,#aab3bb)}
.member:nth-child(2) .member-photo{background:linear-gradient(180deg,#e4eef6,#b6c6d3)}
.member:nth-child(3) .member-photo{background:linear-gradient(180deg,#f0f1f2,#b9bec3)}
.member:nth-child(4) .member-photo{background:linear-gradient(180deg,#e8ebee,#a5adb5)}
.member h4{font-family:"Open Sans",sans-serif;font-size:11px;font-weight:600;color:#666;margin:10px 0 4px}

/* feature */
.feature{height:430px;padding-top:30px;border-top:1px solid var(--line)}
.feature .wrap{display:flex;gap:90px}
.feature-image{width:380px;height:340px;background:linear-gradient(160deg,#dfe3e7 0%,#5b7590 45%,#2a4a6b 75%,#d4d8dc 100%)}
.feature-copy{padding-top:70px;width:460px}
.feature-copy h2{font-size:26px;font-weight:700;color:var(--blue-deep)}
.feature-copy h3{font-size:19px;color:#444;margin-top:2px}
.feature-copy p{font-size:12px;margin-top:14px}
.checks{list-style:none;margin-top:14px}
.checks li{display:flex;align-items:center;gap:10px;font-size:12px;margin-bottom:8px}

/* footer */
.site-footer{height:232px;background:var(--blue);color:var(--white);padding-top:34px}
.site-footer .wrap{display:flex;justify-content:space-between}
.site-footer h4{color:var(--white);font-size:15px;font-weight:500;letter-spacing:.5px;margin-bottom:12px}
.site-footer p,.site-footer li{font-size:11.5px;color:#e6f4fb}
.footer-col{width:280px}
.contact-line{display:flex;align-items:center;gap:8px;margin-top:8px}
.feed{list-style:none}
.feed li{display:flex;gap:10px;margin-bottom:12px}
.newsletter form{display:flex;margin-top:14px}
.newsletter .field{flex:1;height:32px;background:var(--white)}
.newsletter .btn-dark{background:#111;color:var(--white);font-size:11px;font-weight:600;padding:0 16px;display:flex;align-items:center}
.footer-bottom{height:52px;background:var(--blue-deep);color:#d6e6f5;font-size:11px;text-align:center;line-height:52px}
</style>
</head>
<body>

<header class="site-header">
  <div class="wrap">
    <div class="brand"><span class="brand-square"></span>Copper Lantern Consulting</div>
    <nav class="main-nav">
      <a href="#">HOME</a><a href="#">ABOUT US</a><a href="#">OUR SERVICES</a><a href="#">BLOG</a><a href="#">CONTACT US</a>
    </nav>
  </div>
</header>

<section class="hero">
  <div class="hero-photo" role="img" aria-label="Photo of a businessman in a suit working at a laptop in a bright office"></div>
  <div class="hero-copy">
    <h1>COPPER LANTERN <span>CONSULTING</span></h1>
    <p>We shape search, social and paid media plans that bring steady growth to ambitious businesses across the region and beyond.</p>
  </div>
  <div class="slide-arrow prev"><svg width="10" height="14" viewBox="0 0 10 14"><path d="M8 1 2 7l6 6" fill="none" stroke="#fff" stroke-width="2"/></svg></div>
  <div class="slide-arrow next"><svg width="10" height="14" viewBox="0 0 10 14"><path d="M2 1l6 6-6 6" fill="none" stroke="#fff" stroke-width="2"/></svg></div>
</section>

<section class="welcome">
  <div class="wrap">
    <h2>Welcome To <span>Copper Lantern Consulting</span></h2>
    <a class="btn" href="#">MORE INFO</a>
    <p>Copper Lantern Consulting helps business owners and decision makers turn online attention into real results. Our team blends search optimisation, social media strategy and paid advertising into one clear plan, measured every month and tuned as markets shift. We keep reporting simple, so you always know what works and why.</p>
  </div>
</section>

<section class="services">
  <div class="wrap">
    <h2>Our Services</h2>
    <p class="intro">From the first audit to the final report, we cover every channel your customers use. Each service is built around clear goals, honest numbers and a steady pace of improvement.</p>
    <div class="service-grid">
      <div class="service">
        <div class="service-icon"><svg width="46" height="46" viewBox="0 0 46 46"><circle cx="19" cy="19" r="12" fill="none" stroke="#fff" stroke-width="5"/><path d="M28 28l12 12" stroke="#fff" stroke-width="7" stroke-linecap="round"/></svg></div>
        <h3>SEO SERVICE</h3>
        <p>Technical audits, keyword research and content that climbs the search rankings.</p>
      </div>
      <div class="service">
        <div class="service-icon"><svg width="46" height="46" viewBox="0 0 46 46"><path d="M6 14h10a5 5 0 1 1 10 0h10v10a5 5 0 1 1 0 10v8H6V30a5 5 0 1 0 0-10z" fill="#fff"/></svg></div>
        <h3>SOCIAL MEDIA CAMPAIGN</h3>
        <p>Campaigns that grow engaged followers and turn conversations into qualified leads.</p>
      </div>
      <div class="service">
        <div class="service-icon"><svg width="48" height="46" viewBox="0 0 48 46"><rect x="4" y="6" width="40" height="26" rx="2" fill="none" stroke="#fff" stroke-width="4"/><path d="M18 40h12M24 32v8" stroke="#fff" stroke-width="4"/></svg></div>
        <h3>PPC SERVICE</h3>
        <p>Paid search and display ads managed daily for the best return on spend.</p>
      </div>
      <div class="service">
        <div class="service-icon"><svg width="46" height="46" viewBox="0 0 46 46"><circle cx="23" cy="23" r="18" fill="none" stroke="#fff" stroke-width="4"/><ellipse cx="23" cy="23" rx="8" ry="18" fill="none" stroke="#fff" stroke-width="3"/><path d="M5 23h36M9 13h28M9 33h28" stroke="#fff" stroke-width="3"/></svg></div>
        <h3>ONLINE SERVICES</h3>
        <p>Websites, email and analytics that tie every channel into one clear picture.</p>
      </div>
    </div>
  </div>
</section>

<section class="testimonial">
  <div class="testimonial-photo" role="img" aria-label="Dark photo of a city skyline at dusk"></div>
  <div class="wrap">
    <div class="quote-mark">&#8220;</div>
    <p>Working with this team changed how we think about marketing. Our search traffic doubled within six months, our ad costs fell, and for the first time we can see exactly where every new customer comes from. Clear advice, quick answers and real results.</p>
    <div class="dots"><i class="on"></i><i></i><i></i></div>
    <span class="t-arrow prev">&#171;</span><span class="t-arrow next">&#187;</span>
  </div>
</section>

<section class="team">
  <div class="wrap team-grid">
    <div class="member"><div class="member-photo" role="img" aria-label="Portrait photo of a team member"></div><h4>JOHN DOE, PhD.</h4></div>
    <div class="member"><div class="member-photo" role="img" aria-label="Portrait photo of a team member"></div><h4>JOHN DOE, PhD.</h4></div>
    <div class="member"><div class="member-photo" role="img" aria-label="Portrait photo of a team member"></div><h4>JOHN DOE, PhD.</h4></div>
    <div class="member"><div class="member-photo" role="img" aria-label="Portrait photo of a team member"></div><h4>JOHN DOE, PhD.</h4></div>
  </div>
</section>

<section class="feature">
  <div class="wrap">
    <div class="feature-image" role="img" aria-label="Product photo of a desktop computer showing a search marketing scene"></div>
    <div class="feature-copy">
      <h2>COPPER LANTERN CONSULTING</h2>
      <h3>Feature our services</h3>
      <p>Every plan starts with listening. We learn your goals, study your market and build a roadmap that fits your budget and your timeline.</p>
      <ul class="checks">
        <li><svg width="12" height="12" viewBox="0 0 12 12"><path d="M1 6l3.5 3.5L11 2" fill="none" stroke="#0293ce" stroke-width="2.2"/></svg>Search engine optimisation</li>
        <li><svg width="12" height="12" viewBox="0 0 12 12"><path d="M1 6l3.5 3.5L11 2" fill="none" stroke="#0293ce" stroke-width="2.2"/></svg>Social media campaigns</li>
        <li><svg width="12" height="12" viewBox="0 0 12 12"><path d="M1 6l3.5 3.5L11 2" fill="none" stroke="#0293ce" stroke-width="2.2"/></svg>Pay per click advertising</li>
        <li><svg width="12" height="12" viewBox="0 0 12 12"><path d="M1 6l3.5 3.5L11 2" fill="none" stroke="#0293ce" stroke-width="2.2"/></svg>Web design and analytics</li>
      </ul>
    </div>
  </div>
</section>

<footer class="site-footer">
  <div class="wrap">
    <div class="footer-col">
      <h4>CONTACT US</h4>
      <p>Copper Lantern Consulting<br>Harbor Point, OR 97400</p>
      <div class="contact-line"><svg width="12" height="12" viewBox="0 0 12 12"><path d="M2 1h3l1 3-1.5 1a6 6 0 0 0 2.5 2.5L8 6l3 1v3c0 .6-.4 1-1 1A9 9 0 0 1 1 2c0-.6.4-1 1-1z" fill="#fff"/></svg><p>+1 (555) 014-2286</p></div>
      <div class="contact-line"><svg width="12" height="10" viewBox="0 0 12 10"><rect x=".5" y=".5" width="11" height="9" fill="none" stroke="#fff"/><path d="M.5 .5 6 5l5.5-4.5" fill="none" stroke="#fff"/></svg><p>hello@copperlantern.example</p></div>
    </div>
    <div class="footer-col">
      <h4>LATEST RSS FEEDS</h4>
      <ul class="feed">
        <li><svg width="14" height="14" viewBox="0 0 14 14" style="flex:none;margin-top:3px"><rect width="14" height="14" fill="#fff"/></svg>Five quick changes that lift your local search rankings this spring, explained step by step.</li>
        <li><svg width="14" height="14" viewBox="0 0 14 14" style="flex:none;margin-top:3px"><rect width="14" height="14" fill="#fff"/></svg>How to set a sensible pay per click budget for a small business.</li>
      </ul>
    </div>
    <div class="footer-col newsletter">
      <h4>NEWSLETTER</h4>
      <p>Get our monthly notes on search, social and paid media straight to your inbox.</p>
      <form><span class="field"></span><span class="btn-dark">Sign Up</span></form>
    </div>
  </div>
</footer>
<div class="footer-bottom">2015 All Rights Reserved. Copper Lantern Consulting</div>

</body>
</html>
```